Business Card Design for Kidvale (Hires out childrens play areas)

Looking to have a business card designed for a company we just bought. The company rents out childrens play areas.

I have uploaded a couple of examples of the kind of business card style I like. Here are two more examples:

https://quorvastudio.nz/project/bright-romp-branding/
https://imgvaultcdn.com/design_img/8841052/302917/302917_5518203_8841052_b73e19a2_image.jpg

I think a white card will be best due to all the colours in the logo.

Size we require: 3.75" x 2.25" (horizontally orientated) with a 0.125" bleed

Uploaded is two versions of our logo.

Details for the card:
1. My name: Liam Verster
2. Title: Managing Director
3. Phone no: 021 563 417
4. Email: liam@kidvale.co.nz
5. URL: www.kidvale.co.nz
6. Address:
PO Box 318625
Fernlea, Auckland

Let me know if you need anything else.

Target Market(s)

Hospitals, doctors surgeries, bed shops, etc.

Contact Information for Business Card

Details for the card:
1. My name: Liam Verster
3. Phone no: 021 563 417
5. URL: www.kidvale.co.nz
6. Address:
PO Box 318625
Fernlea, Auckland

Requirements
Should not have
• Not too busy.

```html
<!DOCTYPE html>
<html lang="en">
<head>
<meta charset="utf-8">
<title>Kidvale Business Card</title>
<link rel="stylesheet" href="https://fonts.googleapis.com/css2?family=Questrial&display=swap">
<style>
  :root {
    --stage: #e4e4e4;
    --card-white: #fbfbfb;
    --brand-blue: #0a5aa8;
    --brand-purple: #8a2a8e;
    --ink: #141414;
    --faint-lilac: #eadcee;
    --card-font: "Questrial", sans-serif;
  }
  * { margin: 0; padding: 0; box-sizing: border-box; }
  html, body { width: 1200px; height: 864px; overflow: hidden; }
  body { background: var(--stage); font-family: var(--card-font); position: relative; }

  .card {
    position: absolute;
    width: 560px;
    height: 336px;
    background: var(--card-white);
    box-shadow: 0 6px 18px rgba(0,0,0,0.15);
    overflow: hidden;
  }
  .card--back { left: 580px; top: 96px; }
  .card--front { left: 60px; top: 432px; }

  /* back side */
  .back-mark {
    position: absolute; left: 50%; top: 50%;
    width: 230px; height: 230px; margin: -115px 0 0 -115px;
    border-radius: 50%; background: var(--faint-lilac);
  }
  .back-wordmark {
    position: absolute; left: 0; right: 0; top: 50%;
    transform: translateY(-50%);
    text-align: center; font-size: 58px; color: var(--brand-blue);
  }

  /* front side */
  .front-art { position: absolute; inset: 0; }
  .front-wordmark {
    position: absolute; left: 130px; width: 300px; top: 42px;
    text-align: center; font-size: 50px; color: var(--brand-blue);
  }
  .holder { position: absolute; left: 200px; top: 132px; }
  .holder-name { font-size: 32px; color: var(--ink); line-height: 1; }
  .holder-title { font-size: 17px; color: var(--brand-purple); margin-top: 6px; margin-left: 2px; }

  .contact { position: absolute; color: #fff; font-size: 15px; line-height: 1.25; }
  .contact-row { display: flex; align-items: flex-start; gap: 9px; margin-bottom: 7px; }
  .contact--left { left: 26px; top: 232px; }
  .contact--right { right: 26px; top: 262px; text-align: right; }
  .contact--right .contact-row { justify-content: flex-end; }
  .icon { width: 18px; height: 18px; flex: none; margin-top: 1px; }
</style>
</head>
<body>

  <section class="card card--back" aria-label="Card back">
    <div class="back-mark"></div>
    <div class="back-wordmark">Kidvale</div>
  </section>

  <section class="card card--front" aria-label="Card front">
    <svg class="front-art" viewBox="0 0 560 336" width="560" height="336" aria-hidden="true">
      <rect width="560" height="336" fill="var(--brand-blue)"/>
      <path d="M14,0 C26,175 190,236 330,232 C440,229 510,196 560,158 V0 Z" fill="var(--brand-purple)"/>
      <path d="M30,0 C56,160 200,222 330,222 C440,222 512,190 560,156 V0 Z" fill="var(--card-white)"/>
    </svg>

    <div class="front-wordmark">Kidvale</div>

    <div class="holder">
      <div class="holder-name">Liam Verster</div>
      <div class="holder-title">Managing Director</div>
    </div>

    <div class="contact contact--left">
      <div class="contact-row">
        <svg class="icon" viewBox="0 0 18 18"><rect width="18" height="18" rx="3" fill="#fff"/><circle cx="9" cy="9" r="5.5" fill="none" stroke="var(--brand-blue)" stroke-width="1.4"/><path d="M3.5 9h11M9 3.5c-2.5 3-2.5 8 0 11M9 3.5c2.5 3 2.5 8 0 11" fill="none" stroke="var(--brand-blue)" stroke-width="1.2"/></svg>
        <span>www.kidvale.co.nz</span>
      </div>
      <div class="contact-row">
        <svg class="icon" viewBox="0 0 18 18"><rect width="18" height="18" rx="3" fill="#fff"/><path d="M9 15s-4.5-4.6-4.5-7.6a4.5 4.5 0 0 1 9 0C13.5 10.4 9 15 9 15z" fill="var(--brand-blue)"/><circle cx="9" cy="7.4" r="1.7" fill="#fff"/></svg>
        <span>PO Box 318625<br>Fernlea, Auckland</span>
      </div>
    </div>

    <div class="contact contact--right">
      <div class="contact-row">
        <span>021 563 417</span>
        <svg class="icon" viewBox="0 0 18 18"><rect width="18" height="18" rx="3" fill="#fff"/><path d="M5.2 3.5l2.3 2.6-1.2 1.6c.8 1.7 2.1 3 3.8 3.8l1.6-1.2 2.6 2.3-1.3 1.9C8.4 14.3 3.7 9.6 3.5 5z" fill="var(--brand-blue)"/></svg>
      </div>
      <div class="contact-row">
        <span>liam@kidvale.co.nz</span>
        <svg class="icon" viewBox="0 0 18 18"><rect width="18" height="18" rx="3" fill="#fff"/><rect x="3" y="5" width="12" height="8.5" fill="none" stroke="var(--brand-blue)" stroke-width="1.4"/><path d="M3 5l6 5 6-5" fill="none" stroke="var(--brand-blue)" stroke-width="1.4"/></svg>
      </div>
    </div>
  </section>

</body>
</html>
```